I am a company selling interior designing materials

HI, I am selling interior design materials and require a namecard which is more outstanding while following a certain details placement as attached.

My clients are mainly interior designers so it has to attract their attention rather than feeling that its "just another namecard". I am selling wallcoverings, fabrics, acoustics and carpets.

Target Market(s)

interior designers designing hotels, commerical offices.

Contact Information for Business Card

As per attached.
Please change address to 47 Jalan 16 Tampines #05-02 Velmora Building Singapore 527314

Font styles to use
Other font styles liked:
• calibri

Requirements
Must have
• (1) company logo on top in the middle. Placement of contac details to be the same
• (2) company color is blue/green cymk 75/8/42/0
• (3) "KTV" logo to be prominent
• (4) You may change the logo but there should be a "swirl" surrounding the word KTV like current logo. The swirl pattern does not need to follow current logo and you may propose.
Should not have
• (1) there should not be any designs above "KTV" logo
• (2) no sharp triangles or angles

```html
<!DOCTYPE html>
<html lang="en">
<head>
<meta charset="utf-8">
<title>KTV Name Card – Front and Back</title>
<link rel="stylesheet" href="https://fonts.googleapis.com/css2?family=Carlito:wght@400;700&family=Noto+Serif:wght@700&family=Open+Sans:wght@700&display=swap">
<style>
  :root {
    --paper: #ffffff;
    --frame: #555555;
    --crop: #333333;
    --brand-teal: #3fb1a4;
    --brand-red: #e0141f;
    --brand-grey: #6d6e70;
    --wave-light: #9a0f17;
    --wave-dark: #5c0006;
    --on-wave: #ffffff;
  }
  html, body {
    margin: 0;
    padding: 0;
    width: 764px;
    height: 1200px;
    overflow: hidden;
    background: var(--paper);
  }
  .card-sheet {
    display: block;
    width: 764px;
    height: 1200px;
  }
  .sheet-frame { fill: none; stroke: var(--frame); stroke-width: 0.8; }
  .crop-marks line { stroke: var(--crop); stroke-width: 0.6; }
  .wave-band { fill: url(#waveFill); }
  .brand-mark { font-family: "Carlito", "Calibri", sans-serif; font-weight: 700; fill: var(--brand-grey); }
  .brand-dot { fill: var(--brand-teal); }
  .company-name { font-family: "Noto Serif", Georgia, serif; font-weight: 700; font-size: 8px; fill: var(--brand-teal); }
  .person-name { font-family: "Noto Serif", Georgia, serif; font-weight: 700; font-size: 40px; fill: var(--brand-red); }
  .mobile-number { font-family: "Open Sans", "Carlito", sans-serif; font-weight: 700; font-size: 22px; fill: var(--brand-grey); }
  .contact-line { font-family: "Carlito", "Calibri", sans-serif; font-weight: 700; font-size: 11.5px; fill: var(--on-wave); }
  .product-line { font-family: "Noto Serif", Georgia, serif; font-weight: 700; font-size: 19px; fill: var(--on-wave); }
</style>
</head>
<body>
<svg class="card-sheet" viewBox="0 0 553 868.6" preserveAspectRatio="none" xmlns="http://www.w3.org/2000/svg" aria-label="KTV name card, front and back">
  <defs>
    <linearGradient id="waveFill" x1="0" y1="0" x2="1" y2="0">
      <stop offset="0" stop-color="var(--wave-light)"/>
      <stop offset="1" stop-color="var(--wave-dark)"/>
    </linearGradient>
    <g id="cropSet" class="crop-marks">
      <line x1="8" y1="52" x2="52" y2="52"/><line x1="8" y1="65" x2="52" y2="65"/>
      <line x1="52" y1="8" x2="52" y2="52"/><line x1="65" y1="8" x2="65" y2="52"/>
      <line x1="500" y1="52" x2="544" y2="52"/><line x1="500" y1="65" x2="544" y2="65"/>
      <line x1="487" y1="8" x2="487" y2="52"/><line x1="500" y1="8" x2="500" y2="52"/>
      <line x1="8" y1="320" x2="52" y2="320"/><line x1="8" y1="333" x2="52" y2="333"/>
      <line x1="52" y1="333" x2="52" y2="377"/><line x1="65" y1="333" x2="65" y2="377"/>
      <line x1="500" y1="320" x2="544" y2="320"/><line x1="500" y1="333" x2="544" y2="333"/>
      <line x1="487" y1="333" x2="487" y2="377"/><line x1="500" y1="333" x2="500" y2="377"/>
      <line x1="218" y1="35" x2="335" y2="35"/><line x1="218" y1="350" x2="335" y2="350"/>
      <line x1="37" y1="135" x2="37" y2="250"/><line x1="8" y1="192" x2="45" y2="192"/>
      <line x1="516" y1="135" x2="516" y2="250"/><line x1="508" y1="192" x2="544" y2="192"/>
    </g>
  </defs>

  <!-- Front -->
  <g class="card-front">
    <rect class="sheet-frame" x="7" y="7" width="538" height="371"/>
    <path class="wave-band" d="M52,237 C120,212 210,232 300,262 C385,290 440,268 500,152 L500,333 L52,333 Z"/>
    <use href="#cropSet"/>
    <circle class="brand-dot" cx="243" cy="96" r="4"/>
    <text class="brand-mark" x="279" y="104" text-anchor="middle" font-size="25">KTV</text>
    <text class="company-name" x="276" y="132" text-anchor="middle">KaTaVia Interior Furnishings Pte Ltd</text>
    <text class="person-name" x="276" y="192" text-anchor="middle">Lydia Tan</text>
    <text class="mobile-number" x="276" y="222" text-anchor="middle">(65) 9721 4053</text>
    <text class="contact-line" x="79" y="292">47 Jalan 16 Tampines #05-02</text>
    <text class="contact-line" x="79" y="308">Velmora Building Singapore 527314</text>
    <text class="contact-line" x="472" y="292" text-anchor="end">(65) 6382 7145</text>
    <text class="contact-line" x="472" y="308" text-anchor="end">lydia@ktvfurnishings.com</text>
  </g>

  <!-- Back -->
  <g class="card-back" transform="translate(0,483)">
    <rect class="sheet-frame" x="7" y="7" width="538" height="372"/>
    <path class="wave-band" d="M52,233 C120,208 210,228 300,258 C385,286 440,262 500,150 L500,335 L52,335 Z"/>
    <use href="#cropSet"/>
    <circle class="brand-dot" cx="180" cy="145" r="11"/>
    <text class="brand-mark" x="282" y="171" text-anchor="middle" font-size="72">KTV</text>
    <text class="product-line" x="82" y="309">Wallcoverings</text>
    <text class="product-line" x="231" y="309">Acoustic</text>
    <text class="product-line" x="326" y="309">Fabrics</text>
    <text class="product-line" x="409" y="309">Carpet</text>
  </g>
</svg>
</body>
</html>
```